pelmora.com

Design proposals for a gold bank site and gold wallet main page. The site will let people (and companies) open accounts and purchase gold for deposit and later make payments with the gold they hold in the bank. The bank will be a e-money licensed venture located in Switzerland. The functionality of the "system" will be very simple and possibly only use icon symbols so it can be multilingual.

The mainstays of the site will be security and trust. Al digital gold is backed 100 % by visible gold in vault audited every day.

Target Market(s)

Asian and American gold buyers and people preferring gold to currency

Industry/Entity Type

Security

Requirements
Must have
• a) Logo
b) Main index page with a new logo and design
c) System (post log in e-wallet) main page showing the last transactions of the client and give client options to transfer funds and make deposits
Nice to have
• sample contact form
sample faq page
terms page design
Should not have
• So much text since it will be aimed at the worldwide market

```html
<!DOCTYPE html>
<html lang="en">
<head>
<meta charset="utf-8">
<title>Pelmora – Gold Bank</title>
<link href="https://fonts.googleapis.com/css2?family=Roboto+Condensed:wght@300;400&family=Arimo:wght@400&display=swap" rel="stylesheet">
<style>
:root{
  --gold:#f6d500;
  --gold-deep:#f5b800;
  --ink:#1b1b1b;
  --paper:#f3f3f3;
  --text:#666;
  --heading:#333;
  --footer:#2a2a2b;
  --footer-bottom:#1d1d1e;
  --footer-text:#e6e6e6;
  --muted:#8a8a8a;
  --panel:#ebe9e4;
}
*{box-sizing:border-box;margin:0;padding:0}
html,body{width:1184px;height:1200px;overflow:hidden}
body{position:relative;background:var(--paper);font-family:"Arimo",Arial,sans-serif;color:var(--text)}
.site-header{position:absolute;left:0;top:0;width:1184px;height:63px;background:var(--gold)}
.brand{position:absolute;left:139px;top:0;width:242px;height:63px;background:var(--ink);clip-path:polygon(18px 0,100% 0,calc(100% - 18px) 100%,0 100%);display:flex;align-items:center;padding-left:38px;gap:10px}
.brand-dot{width:26px;height:26px;border-radius:50%;background:var(--gold-deep)}
.brand-name{font-family:"Roboto Condensed",sans-serif;font-weight:400;font-size:30px;color:var(--gold);letter-spacing:1px}
.main-nav{position:absolute;left:396px;top:20px;display:flex}
.main-nav a{font-family:"Roboto Condensed",sans-serif;font-size:16px;color:#333;text-decoration:none;margin-right:36px}
.hero{position:absolute;left:0;top:63px;width:1184px;height:420px}
.hero-bg{position:absolute;inset:0}
.hero-photo{position:absolute;left:139px;top:46px;width:670px;height:316px;border:4px solid #b9b9b9;background:radial-gradient(ellipse at 50% 55%,#ffcc30 0%,#f08a10 55%,#c94e05 100%)}
.hero-bubble{position:absolute;left:815px;top:116px;width:228px;height:270px}
.hero-bubble span{position:absolute;left:0;top:64px;width:228px;text-align:center;font-family:"Roboto Condensed",sans-serif;font-weight:300;font-size:22px;color:var(--gold)}
.content{position:absolute;left:139px;top:0;width:611px;height:950px}
.content > *{position:absolute;left:0}
.section-title{width:611px;font-family:"Roboto Condensed",sans-serif;font-weight:300;font-size:19px;line-height:22px;color:var(--heading);padding-bottom:4px;border-bottom:1px dotted #aaa}
.content p{width:611px;font-size:11px;line-height:19px;color:var(--text)}
.btn-more{display:block;background:linear-gradient(#ffd84a,var(--gold-deep));font-size:11px;line-height:14px;color:#333;padding:4px 10px}
.faq-q{font-family:"Roboto Condensed",sans-serif;font-weight:300;font-size:15px;line-height:18px;color:var(--heading)}
.quick-contact{position:absolute;left:768px;top:521px;width:277px;height:295px;background:var(--panel);border:2px solid #dcd9d2;padding:16px 13px}
.quick-contact h3{font-family:"Roboto Condensed",sans-serif;font-weight:400;font-size:16px;color:var(--heading);margin-bottom:13px}
.field{display:block;width:230px;height:27px;border:1px solid #ccc;border-radius:14px;background:#fff;font-size:11px;color:#555;padding:7px 12px;margin-bottom:8px;box-shadow:inset 0 1px 2px rgba(0,0,0,.08)}
.field.message{height:78px;border-radius:12px}
.btn-submit{display:inline-block;margin-top:9px;padding:6px 18px;border-radius:16px;background:linear-gradient(#ffe14a,var(--gold-deep));border:1px solid #fff;box-shadow:0 0 0 1px #e3c25a;font-family:"Roboto Condensed",sans-serif;font-size:15px;color:#222}
.open-account{position:absolute;left:768px;top:833px;width:275px;height:86px;border:2px solid var(--gold-deep);box-shadow:0 2px 4px rgba(0,0,0,.2);background:linear-gradient(100deg,#caa12a 0%,#f2c417 45%,#ffd000 100%);display:flex;align-items:center;padding-left:13px}
.open-account span{font-family:"Roboto Condensed",sans-serif;font-weight:400;font-size:30px;color:#222}
.open-account svg{margin-left:10px}
.site-footer{position:absolute;left:0;top:950px;width:1184px;height:210px;background:var(--footer)}
.footer-col{position:absolute;top:24px;height:180px;padding-left:1px}
.footer-col+.footer-col{border-left:1px solid #3a3a3b;padding-left:12px}
.footer-col h4{font-family:"Roboto Condensed",sans-serif;font-weight:400;font-size:14px;color:var(--gold);margin-bottom:10px}
.footer-col li{list-style:none;font-size:11px;color:var(--footer-text);line-height:21.3px}
.social{display:flex;align-items:center;gap:9px;font-size:11px;color:var(--footer-text);margin-bottom:14px}
.social-dot{width:29px;height:29px;border-radius:50%;background:#4f7fc0}
.social-dot.alt{background:#7fb9e4}
.contact-line{display:flex;align-items:center;gap:12px;font-size:11px;color:var(--footer-text);margin-bottom:14px;padding-left:4px}
.footer-bottom{position:absolute;left:0;top:1160px;width:1184px;height:40px;background:var(--footer-bottom);font-size:11px;color:var(--muted);padding:11px 0 0 140px}
.footer-bottom .sep{margin:0 9px 0 22px}
</style>
</head>
<body>
<header class="site-header">
  <div class="brand"><span class="brand-dot"></span><span class="brand-name">PELMORA</span></div>
  <nav class="main-nav">
    <a href="#">Home</a><a href="#">About us</a><a href="#">Buy Gold</a><a href="#">Sell Gold</a><a href="#">Faqs</a><a href="#">Contact us</a>
  </nav>
</header>

<section class="hero">
  <svg class="hero-bg" width="1184" height="420" viewBox="0 0 1184 420" aria-hidden="true">
    <defs>
      <linearGradient id="heroShade" x1="0" y1="0" x2="0" y2="1">
        <stop offset="0" stop-color="#2a2a2a"/><stop offset="1" stop-color="#151515"/>
      </linearGradient>
    </defs>
    <path fill="url(#heroShade)" d="M0 0H1184V380L1160 374 1130 386 1090 378 1050 392 1010 384 960 398 920 390 880 402 840 392 800 398 760 392 720 400 680 392 640 396 600 390 560 370 530 386 490 384 450 392 400 386 360 392 320 394 280 386 240 390 200 380 160 394 120 380 90 372 60 386 30 380 0 384Z"/>
  </svg>
  <div class="hero-photo" role="img" aria-label="Photo of stacked one-kilo gold bars"></div>
  <div class="hero-bubble">
    <svg width="228" height="270" viewBox="0 0 228 270" aria-hidden="true">
      <path fill="#050505" d="M114 0C176 0 224 42 224 96 224 150 180 186 120 186 96 186 84 196 72 230 66 202 40 190 20 178 4 160 0 130 0 96 0 42 52 0 114 0Z"/>
    </svg>
    <span>Why buy Gold?</span>
  </div>
</section>

<main class="content">
  <h2 class="section-title" style="top:495px">Buy Gold Coins</h2>
  <p style="top:536px">Lorem Ipsum is simply dummy text of the printing and typesetting industry. Lorem Ipsum has been the industry's stan-<br>dard dummy text ever since the 1500s,</p>
  <p style="top:585px">Lorem Ipsum is simply dummy text of the printing and typesetting industry. Lorem Ipsum has been the industry's stan-<br>dard dummy text ever since the 1500s,</p>
  <span class="btn-more" style="top:638px">+ Show More</span>
  <h2 class="section-title" style="top:674px">FAQ</h2>
  <h3 class="faq-q" style="top:716px">Why should you invest in gold?</h3>
  <p style="top:740px">Lorem Ipsum is simply dummy text of the printing and typesetting industry. Lorem Ipsum has been the industry's stan-<br>dard dummy text ever since the 1500s,</p>
  <h3 class="faq-q" style="top:800px">In what sizes are the Gold coins / bars available?</h3>
  <p style="top:824px">Lorem Ipsum is simply dummy text of the printing and typesetting industry. Lorem Ipsum has been the industry's stan-<br>dard dummy text ever since the 1500s,</p>
  <span class="btn-more" style="top:912px">+ Show More</span>
</main>

<aside class="quick-contact">
  <h3>Quick Contact</h3>
  <span class="field">Name</span>
  <span class="field">Email</span>
  <span class="field">Phone</span>
  <span class="field message">Message</span>
  <span class="btn-submit">SUBMIT</span>
</aside>

<div class="open-account" role="img" aria-label="Gold payment card image behind an open-account call to action">
  <span>Open your account</span>
  <svg width="20" height="28" viewBox="0 0 20 28" aria-hidden="true"><path d="M4 3L15 14 4 25" fill="none" stroke="#333" stroke-width="5"/></svg>
</div>

<footer class="site-footer">
  <div class="footer-col" style="left:139px;width:241px">
    <h4>Main Links</h4>
    <ul><li>Home</li><li>About us</li><li>FAs</li><li>Contact</li></ul>
  </div>
  <div class="footer-col" style="left:361px;width:223px">
    <h4>Services</h4>
    <ul><li>Buy Gold</li><li>Sell Gold</li><li>How to buy</li><li>Open a Account</li><li>Market Updates</li><li>Customer Service Point</li></ul>
  </div>
  <div class="footer-col" style="left:584px;width:223px">
    <h4>Get In Touch</h4>
    <div class="social"><span class="social-dot"></span>Follow us on Lumigram</div>
    <div class="social"><span class="social-dot alt"></span>Follow us on Chirpline</div>
  </div>
  <div class="footer-col" style="left:807px;width:240px">
    <h4>Contact</h4>
    <div class="contact-line">
      <svg width="14" height="14" viewBox="0 0 14 14" aria-hidden="true"><path fill="#ddd" d="M3 0L6 3 4.5 5C5.5 7 7 8.5 9 9.5L11 8 14 11 12 13.5C6 14 0 8 0.5 2Z"/></svg>
      +1 555 0142
    </div>
    <div class="contact-line">
      <svg width="16" height="12" viewBox="0 0 16 12" aria-hidden="true"><rect x="0.5" y="0.5" width="15" height="11" fill="#cfe0f2" stroke="#8aa7c8"/><path d="M1 1L8 7 15 1" fill="none" stroke="#6b8db3"/></svg>
      hello@pelmora.com
    </div>
  </div>
</footer>
<div class="footer-bottom">© 2010 Pelmora. All Rights Reserved.<span class="sep">|</span>Terms &amp; Conditions<span class="sep" style="margin-left:10px">|</span>Privacy Policy</div>
</body>
</html>
```